Vorlen - Customer Experience Software Company Web Design

*****UPDATE*****
We've been getting a lot of corporate designs through. Unfortunately this is not what we are looking for. We would like our brand to be more approachable and for the look and feel to to be a bit more fun.
Also the best designs we have received so far have followed the "less is more" approach. Im hoping any news designs will take these aspects into account.
*****************

Background:

Vorlen is a Customer Experience Technology company. We equip business and technology teams with the frameworks, tools and services to help them create compelling experiences for their customers.

Our flagship product - Vorlen CX is an open-source customer experience application framework – it enables organisation to build highly differentiated business applications to deliver compelling experiences to your customers.

Vorlen CX is designed for innovators who understand that unlocking opportunity in today’s competitive marketplace is driven by delivering a better customer experience.

Task:

We are looking for a web design (we need PSD, no HTML/CSS) for our company site through which to launch our customer experience framework product. The site will be also used as a support site, so the functional aspect of the site is as important as the visual impact for sales.

In order to help us conceptualise ideas and content we have drafted a temporary website using a standard wordpress theme (please see details below). Now we have a general idea of our requirements we like we would like to take it to the next level and get some designs with that professional edge.

Our target market are Enterprise organisations - that is senior members of the business & technology teams (Business General Managers, CTO’s, CIO’s, and Senior Architects and Senior Developers). We want something clean & fresh which is DIFFERENT from the typical corporate technology websites out there. We would like to be seen as more approachable than most large technology companies.

Words we would like to use to describe the finished design:
• Clean (we’re thinking white background with one or two key colours)
• Fresh
• Light
• Modern
• Less is more
• Web 2.0
• Fun but professional (aimed at Enterprise/Large organisations)
• Bold, clear call to action – e.g. Live Demo & Download
• Readable (but Sans Serif)

As we’re a Customer Experience company, the usability of the site is critical. The site must be functional, intuitive & easy to navigate. We want to keep the number of user clicks to the bare minimum possible.

Other aspects, which we would like to incorporate into the site
• Home Page banner slider
• Client logon
• Newsletter sign up
• Social media links – Facebook, LinkedIn (for starters)
• Rich footer links

Some websites we like
• http://brightpanelworks.example - clean, light, modern & intuitive
• http://www.tamsoledrik.example - bold, clear messaging
• http://www.opengridhub.example/markup/emblem - punchy, colourful
• http://postwren.example/ - modern, clear messaging, colourful, rich footer area

Target Market(s)

Enterprise organisations - that is senior members of the business & technology teams (Business General Managers, CTO’s, CIO’s, Senior Devs)

Industry/Entity Type

Business

Requirements
Must have
• - Design Specs: Accepted file formats: During the design phase adobe PSD or JPEG are OK (if you need to upload files), but for the handover we'll need PSD only with all the original layers.
- The width needs to be a size that will work with every size computer screen
- Need to use cross-platform compatible font
- The graphic elements used for the design must be copyright free

Current test site
- URL http://vorlen.example/wp-admin
- username: artmarket
- password: artmarket

IMPORTANT NOTE REGARDING OUR CURRENT TEST SITE:

This is a very basic version of a site to help us generate requirements. This design is only a starting point/input and is not locked in stone i.e. we do not simply want this site simply tweaked around the edges.

We are looking for you to use all of your graphic design skills and experience to create a truly awesome site design!

```html
<!DOCTYPE html>
<html lang="en">
<head>
<meta charset="utf-8">
<title>Vorlen – The Customer Experience Framework</title>
<link rel="stylesheet" href="https://fonts.googleapis.com/css2?family=Yanone+Kaffeesatz:wght@300;400;700&family=Arimo:wght@400;700&display=swap">
<style>
:root{
  --blue:#1a9ee6;
  --blue-deep:#1578c0;
  --page:#f7f7f7;
  --panel:#ffffff;
  --ink:#333333;
  --body:#5a5a5a;
  --muted:#8a8a8a;
  --night:#1c1c1c;
  --grey-btn:#6f6f6f;
  --line:#e2e2e2;
}
*{margin:0;padding:0;box-sizing:border-box}
html,body{width:1200px;height:1109px;overflow:hidden;background:var(--page)}
body{position:relative;font-family:"Arimo",Arial,sans-serif;color:var(--ink)}
.abs{position:absolute}
.backdrop{position:absolute;left:0;top:0}
.brand{left:170px;top:42px}
.brand-name{font-family:"Arimo",sans-serif;font-weight:700;font-size:34px;letter-spacing:2px;color:var(--blue);line-height:1}
.brand-tag{font-size:12px;color:#555;margin-top:3px}
.nav{top:96px;left:0;font-family:"Yanone Kaffeesatz",sans-serif;font-weight:300;font-size:21px;letter-spacing:.5px}
.nav a{position:absolute;color:#3a3a3a;text-decoration:none;white-space:nowrap}
.nav a.current{color:#fff}
.hero-title{left:235px;top:218px;font-family:"Yanone Kaffeesatz",sans-serif;font-weight:700;font-size:32px;color:#3a3a3a}
.hero-sub{left:245px;top:256px;font-family:"Yanone Kaffeesatz",sans-serif;font-weight:400;font-size:24px;color:#3a3a3a}
.slide-arrow{width:38px;height:38px;border-radius:50%;border:1px solid #c8c8c8;background:#fff;display:flex;align-items:center;justify-content:center}
.hero-art{left:517px;top:165px;width:428px;height:259px;border-radius:8px;background:radial-gradient(ellipse at 60% 50%,#3fb6ee 0%,#a9dcf5 45%,rgba(247,247,247,0) 75%)}
.panel{left:143px;top:440px;width:892px;height:452px;background:var(--panel);border-radius:8px}
.intro{left:162px;top:460px;width:540px}
.intro h1{font-family:"Yanone Kaffeesatz",sans-serif;font-weight:400;font-size:24px;color:var(--blue);padding-bottom:2px;border-bottom:1px solid var(--line);display:inline-block;padding-right:8px}
.intro p{font-size:9.3px;line-height:14.3px;color:var(--body);margin-top:13px}
.intro h2{font-size:12.5px;font-weight:400;color:#444;margin-top:12px}
.intro h2 + p{margin-top:10px}
.readmore{left:602px;top:760px;width:96px;height:20px;border-radius:3px;background:linear-gradient(#4ab8f2,var(--blue));color:#fff;font-size:10px;display:flex;align-items:center;justify-content:center;gap:5px}
.divider{left:732px;top:526px;width:1px;height:304px;background:linear-gradient(rgba(220,220,220,0),#dcdcdc 30%,#dcdcdc 70%,rgba(220,220,220,0))}
.demo-art{left:866px;top:468px;width:120px;height:105px;border-radius:6px;background:linear-gradient(160deg,#3a3f78,#8f98c4 50%,#d7d7d7)}
.demo-bubble{left:762px;top:477px;width:96px;height:63px;border-radius:12px;background:linear-gradient(#2a9ad9,var(--blue-deep));color:#fff;font-weight:700;font-size:16px;display:flex;align-items:center;justify-content:center;white-space:nowrap;z-index:2}
.demo-bubble::after{content:"";position:absolute;right:-13px;top:18px;border-left:14px solid #2186c8;border-top:11px solid transparent;border-bottom:11px solid transparent}
.login{left:755px;top:590px;width:258px;height:181px;border:1px solid #d4d4d4;border-radius:5px;background:#f4f4f4;overflow:hidden}
.login-head{height:29px;background:linear-gradient(#6d6d6d,#3d3d3d);color:#fff;font-family:"Yanone Kaffeesatz",sans-serif;font-size:20px;padding:2px 0 0 18px}
.field{position:absolute;font-size:10.5px;color:#444;white-space:nowrap}
.field-box{position:absolute;width:166px;height:18px;background:#fff;border:1px solid #e3e3e3}
.check{position:absolute;width:11px;height:11px;border:1px solid #778;background:#fff}
.login-btn{position:absolute;left:84px;top:130px;width:71px;height:19px;border-radius:10px;background:linear-gradient(#555,#2a2a2a);color:#fff;font-family:"Yanone Kaffeesatz",sans-serif;font-size:15px;text-align:center;line-height:19px}
.forgot{position:absolute;left:148px;top:157px;font-size:10px;color:#444}
.newsletter{left:756px;top:785px;width:268px;height:95px;border:1px solid #dcdcdc;border-radius:3px;background:#f1f1f1;text-align:center}
.newsletter h3{font-family:"Yanone Kaffeesatz",sans-serif;font-weight:400;font-size:24px;color:#555;margin-top:12px}
.pill{display:inline-block;background:var(--grey-btn);color:#fff;border-radius:13px;font-family:"Yanone Kaffeesatz",sans-serif;font-size:16px;line-height:24px;padding:0 18px;margin-top:4px}
.follow{left:740px;top:918px;font-family:"Yanone Kaffeesatz",sans-serif;font-size:22px;color:#555}
.social{width:27px;height:27px;border-radius:4px}
.col h4{font-size:13px;font-weight:700;margin-bottom:14px}
.col a{display:block;font-size:11px;color:#a8a8a8;text-decoration:none;line-height:19.6px}
.col.on-dark h4{color:#fff}
.col.on-light h4{color:#222}
.col.on-light a{color:#9a9a9a}
.email{left:760px;top:989px;width:254px;height:27px;border:1px solid #cfcfcf;border-radius:8px;background:#fff;font-size:11px;color:#333;padding:7px 0 0 18px}
.subscribe{left:818px;top:1028px;width:124px;height:23px;border-radius:12px;background:linear-gradient(#8a8a8a,#6b6b6b);color:#fff;font-size:11px;text-align:center;line-height:23px}
.copyright{left:0;width:1200px;top:1088px;text-align:center;font-size:9.5px;color:#9a9a9a}
</style>
</head>
<body>

<svg class="backdrop" width="1200" height="1109" viewBox="0 0 1200 1109" aria-hidden="true">
  <path d="M0,0 H1200 V180 C980,110 760,30 300,8 C180,3 80,2 0,0 Z" fill="#1a9ee6"/>
  <path d="M503,0 H568 V122 Q568,137 553,137 H518 Q503,137 503,122 Z" fill="#1a9ee6"/>
</svg>

<header>
  <div class="abs brand">
    <div class="brand-name">VORLEN</div>
    <div class="brand-tag">The Customer Experience Framework</div>
  </div>
  <nav class="abs nav">
    <a class="current" style="left:516px">HOME</a>
    <a style="left:588px">ABOUT</a>
    <a style="left:672px">PRODUCTS</a>
    <a style="left:788px">SUPPORT</a>
    <a style="left:891px">BLOG</a>
  </nav>
</header>

<section class="hero">
  <div class="abs slide-arrow" style="left:145px;top:280px">
    <svg width="12" height="14" viewBox="0 0 12 14"><path d="M9,1 L3,7 L9,13" fill="none" stroke="#444" stroke-width="2.6"/></svg>
  </div>
  <div class="abs hero-title">Customer Experience</div>
  <div class="abs hero-sub">Application Frame Work</div>
  <div class="abs hero-art" role="img" aria-label="Illustration of a presenter showing a bar chart to a seated audience"></div>
  <div class="abs slide-arrow" style="left:997px;top:280px">
    <svg width="12" height="14" viewBox="0 0 12 14"><path d="M3,1 L9,7 L3,13" fill="none" stroke="#444" stroke-width="2.6"/></svg>
  </div>
</section>

<main>
  <div class="abs panel"></div>

  <article class="abs intro">
    <h1>Create Compelling Experiences For Your Customers</h1>
    <p>Vorlen is a customer experience application framework – it enables you to build highly differentiated business applications<br>to deliver compelling experiences to your customers.</p>
    <p style="margin-top:14px">Vorlen is designed for innovators who understand that unlocking opportunity in today's competitive marketplace is driven by<br>delivering a better customer experience.</p>
    <h2>Opportunity though customer experience innovation</h2>
    <p>Turn the experience you deliver to your customers into competitive advantage. Vorlen's customer experience framework is the flexible and practical way for enterprise organisations to create and manage compelling experiences. It gives you full control over how you wish to interact with your customers, and allows you to tailor experiences that grow your brand.</p>
    <h2>True differentiation</h2>
    <p>There is no one-size-fits-all application, because every business is unique! We believe in technology as a business differentiator, and flexible, cutting edge technology the key to success. If you're serious about differentiation, and want to create powerful experiences to connect with your customers in exciting new ways, we can help create experiences that your competitors can't match.</p>
  </article>
  <div class="abs readmore">
    <svg width="9" height="8" viewBox="0 0 9 8"><path d="M1,1 L4,4 L1,7 M5,1 L8,4 L5,7" fill="none" stroke="#fff" stroke-width="1.2"/></svg>Readmore
  </div>

  <div class="abs divider"></div>

  <aside>
    <div class="abs demo-art" role="img" aria-label="Desktop computer with keyboard and mouse showing the application"></div>
    <div class="abs demo-bubble">Live Demo</div>

    <div class="abs login">
      <div class="login-head">Client Login</div>
      <span class="field" style="left:10px;top:51px">User Name :</span>
      <div class="field-box" style="left:80px;top:47px"></div>
      <span class="field" style="left:12px;top:80px">Password &nbsp;:</span>
      <div class="field-box" style="left:80px;top:76px"></div>
      <div class="check" style="left:87px;top:108px"></div>
      <span class="field" style="left:105px;top:106px">Reminder me</span>
      <div class="login-btn">Login</div>
      <span class="forgot">forgot password ?</span>
    </div>

    <div class="abs newsletter">
      <h3>News Letter Signup</h3>
      <span class="pill">Signup Free</span>
    </div>
  </aside>
</main>

<svg class="backdrop" width="1200" height="1109" viewBox="0 0 1200 1109" aria-hidden="true">
  <defs>
    <linearGradient id="nightFade" x1="0" y1="0" x2="1" y2="0">
      <stop offset="0" stop-color="#151515"/>
      <stop offset="1" stop-color="#333333"/>
    </linearGradient>
  </defs>
  <path d="M0,820 C160,880 320,920 520,960 C760,1010 980,1050 1200,1073 V1109 H0 Z" fill="url(#nightFade)"/>
</svg>

<footer>
  <div class="abs follow">Follow Us</div>
  <div class="abs social" style="left:833px;top:918px;background:#4fb7e8" role="img" aria-label="Social link one"></div>
  <div class="abs social" style="left:871px;top:918px;background:#3b5ea0" role="img" aria-label="Social link two"></div>
  <div class="abs social" style="left:909px;top:918px;background:#1c7ab8" role="img" aria-label="Social link three"></div>

  <div class="abs col on-dark" style="left:220px;top:964px">
    <h4>VORLEN</h4>
    <a>Home</a><a>Products</a><a>Support</a><a>Blog</a><a>About</a>
  </div>
  <div class="abs col on-dark" style="left:376px;top:962px">
    <h4>Getting Started</h4>
    <a>Demo</a><a>Documentation</a><a>Download</a>
  </div>
  <div class="abs col on-light" style="left:577px;top:962px">
    <h4>Support</h4>
    <a>Contact Us</a><a>Vorlen Services</a><a>Vorlen Support</a>
  </div>
  <div class="abs col on-light" style="left:760px;top:961px">
    <h4>Subscribe to Our News Letter</h4>
  </div>
  <div class="abs email">Email Address</div>
  <div class="abs subscribe">Subscribe</div>

  <div class="abs copyright">Copyright © 2011 vorlen.example All Rights Reserved.</div>
</footer>

</body>
</html>
```